Business Stationery Design

I would like to get some stationery designed for my company. The stationery should include a letterhead, envelope, and business card. We are a technology consulting company specializing in Healthcare IT, and Education management systems. The colors of the stationery should match the logo. The logo is uploaded.

Target Market(s)

Hospitals, Clinics. Doctors offices. Private Schools.

Industry/Entity Type

Business

```html
<!DOCTYPE html>
<html lang="en">
<head>
<meta charset="utf-8">
<title>Clearfield Advisory Group – Letterhead</title>
<link rel="stylesheet" href="https://fonts.googleapis.com/css2?family=Lato:wght@400;700&family=Open+Sans:wght@400;600&display=swap">
<style>
  :root {
    --backdrop: #ecebe8;
    --paper: #ffffff;
    --ink: #1e1e1e;
    --brand-green: #6cbf3f;
    --brand-green-faint: #eef5e6;
    --brand-yellow: #f2b31c;
  }
  * { margin: 0; padding: 0; box-sizing: border-box; }
  html, body {
    width: 1112px; height: 1200px; overflow: hidden;
    background: var(--backdrop);
  }
  .letterhead {
    position: absolute; left: 206px; top: 82px;
    width: 705px; height: 996px;
    background: var(--paper);
    overflow: hidden;
    box-shadow: 0 2px 10px rgba(0,0,0,.18);
    color: var(--ink);
    font-family: "Lato", sans-serif;
  }
  .brand-name {
    position: absolute; left: 50px; top: 130px;
    color: var(--brand-green);
    font-family: "Open Sans", sans-serif;
    font-weight: 400;
    font-size: 25px; line-height: 1;
    letter-spacing: -0.3px;
  }
  .brand-name span { display: block; font-size: 10px; letter-spacing: .3px; margin-top: 3px; text-align: right; }
  .contact {
    position: absolute; left: 499px; top: 53px;
    font-family: "Open Sans", sans-serif;
    font-size: 12.5px; line-height: 19px;
    list-style: none;
  }
  .contact li { display: flex; align-items: center; gap: 8px; }
  .contact li.address-line { display: block; }
  .contact svg { width: 14px; height: 14px; flex: none; }
  .decor-circle {
    position: absolute; left: 258px; top: 622px;
    width: 460px; height: 460px; border-radius: 50%;
    background: var(--brand-green-faint);
  }
  .letter-body {
    position: absolute; left: 37px; top: 294px; width: 636px;
    font-size: 13.2px; line-height: 18px;
    text-align: justify;
  }
  .salutation { font-size: 15px; margin-bottom: 16px; text-align: left; }
  .letter-body p + p { margin-top: 17px; }
  .signature {
    position: absolute; left: 36px; top: 612px;
    width: 180px; height: 86px;
    background: linear-gradient(90deg, #e6e6e6, #f2f2f2);
    border-radius: 4px;
  }
  .footer-wave { position: absolute; left: 0; top: 0; width: 705px; height: 996px; }
  .website {
    position: absolute; left: 32px; top: 964px;
    font-family: "Open Sans", sans-serif;
    font-size: 14px; letter-spacing: 1.2px;
    color: var(--ink);
  }
</style>
</head>
<body>
  <main class="letterhead">
    <div class="decor-circle" aria-hidden="true"></div>

    <div class="brand-name">Clearfield<span>Advisory Group</span></div>

    <ul class="contact">
      <li class="address-line">482, Linden Row 9,</li>
      <li class="address-line">Marlow Bay, CA 90210</li>
      <li>
        <svg viewBox="0 0 14 14" aria-hidden="true"><circle cx="7" cy="7" r="7" fill="var(--brand-green)"/><rect x="4.5" y="2.8" width="5" height="8.4" rx="1" fill="none" stroke="#fff" stroke-width="1.2"/></svg>
        555 014 2087
      </li>
      <li>
        <svg viewBox="0 0 14 14" aria-hidden="true"><circle cx="7" cy="7" r="7" fill="var(--brand-green)"/><path d="M4.3 3.5c.6-.5 1.1-.4 1.4.1l.6 1.2c.2.4 0 .8-.3 1 .5 1 1.2 1.7 2.2 2.2.2-.3.6-.5 1-.3l1.2.6c.5.3.6.8.1 1.4-2.8 1.6-7.8-3.4-6.2-6.2z" fill="#fff"/></svg>
        555 014 2087
      </li>
      <li>
        <svg viewBox="0 0 14 14" aria-hidden="true"><circle cx="7" cy="7" r="7" fill="var(--brand-green)"/><rect x="3.3" y="4.3" width="7.4" height="5.4" rx=".6" fill="#fff"/><path d="M3.5 4.6 7 7.4l3.5-2.8" fill="none" stroke="var(--brand-green)" stroke-width=".9"/></svg>
        hello@clearfieldgroup.com
      </li>
    </ul>

    <section class="letter-body">
      <p class="salutation">Dear Mr. Alden,</p>
      <p>Lorem Ipsum is simply dummy text of the printing and typesetting industry. Lorem Ipsum has been the industry's standard dummy text ever since the 1500s, when an unknown printer took a galley of type and scrambled it to make a type specimen book. It has survived not only five centuries, but also the leap into electronic typesetting, remaining essentially unchanged.</p>
      <p>The standard chunk of Lorem Ipsum used since the 1500s is reproduced below for those interested. Sections 1.10.32 and 1.10.33 from "de Finibus Bonorum et Malorum" by Tullius Varen are also reproduced in their exact original form, accompanied by English versions from the 1914 translation by H. Renwick</p>
      <p>Lorem Ipsum is simply dummy text of the printing and typesetting industry. Lorem Ipsum has been the industry's standard dummy text ever since the 1500s, when an unknown printer took a galley of type and scrambled it to make a type specimen book. It has survived not only five centuries, but also the leap into electronic typesetting, remaining essentially unchanged. It was popularised in the</p>
    </section>

    <div class="signature" role="img" aria-label="Handwritten signature of the sender"></div>

    <svg class="footer-wave" viewBox="0 0 705 996" aria-hidden="true">
      <path d="M0,913 C120,895 260,915 380,940 C480,958 600,950 705,933 V996 H0Z" fill="var(--brand-green)"/>
      <path d="M0,944 C140,930 280,946 400,962 C500,975 620,974 705,966 V996 H0Z" fill="var(--brand-yellow)"/>
      <path d="M0,940 C140,926 280,942 400,958 C500,971 620,968 705,957" fill="none" stroke="#fff" stroke-width="2"/>
    </svg>

    <div class="website">www.clearfieldgroup.com</div>
  </main>
</body>
</html>
```